Every Stage Drama Academy Leaflet - Kids classes

I would like a leaflet designed for my classes, with a clear and informative time table on the back:

I have attached a couple of adverts that we have used in the local News Paper and on Chatterbook, and so the front side of the leaflet should be something similar using the plain Star Quest photo:

Wording on the front with the photo should be

'Every Stage Drama Academy Ltd! As featured on The Star Quest Grand Showdown'

Wording 'We offer AFFORDABLE, professional, accredited training in Drama, Singing and Dance for ages 3- 18 years. FREE casting Agency, Optional BRSVE & FQMR exams and Unparalleled performance opportunities.

WWW. EVERYSTAGEDRAMA.EXAMPLE / 020 7946 0718

Chatterbook : www.chatterbook.example/everystagedrama

BOOK your Trial Today!

BACK SIDE

I would like a clear timetable designed with the following info

Classes

Tiny Sparks - Ages 3-5 years - Drama, Singing & Dance
from Pellworth to Pop in one fast paced fun & imaginative session with regular confidence building shows £4

Drama, Song & Dance Ages 6-10 years - 90 minutes of complete theatrical training taught by qualified industry experts with the opportunity to take BRSVE & FQMR Dance exams, regular shows and local events £8.50

Drama, Song & Dance Ages 11- 18years - 90 minutes of advanced level Drama, Singing and Dance. BRSVE & FQMR dance exams , shows, competitions and audition preparation for colleges and castings. This session is a one stop shop for professional theatrical training.

ESD MT ( Musical Theatre) - Ages 6-10years - 90 minutes of Musical Theatre training covering classic musicals including hits such as Marigold, Tollin & Harbour of Drums. Musical Theatre Singing exams and BRSVE drama are included in this popular fast paced session.

ESD MT ( Musical Theatre) - Ages 11- 18years - 90 minutes of professional Musical Theatre training with an emphasis on singing. These Chorale- Style sessions are ideal for those who love musicals such as Hexbound, Jukebox & Grand Ringmaster. Our advanced MT sessions produce high quality songs & medleys for shows and competitions as well as Musical Theatre/ Singing exams and Solo BRSVE training.

Weekend Footlights Company - Ages 4-18years - 4 hours of professional training, working towards a production. This unique group gives young performers the opportunity to perform in a full scale production EVERY term. Past shows include 'Ferry Cousins', 'Kelani', 'Tiny Stall of Frights', 'Anselm & Corabel' and 'Pellworth Heirlines' At ESD we believe that pupils learn through actual performing experience, there is a role for everyone, full costume and the chance to shine on stage!

Day : Tuesdays
Venue: Linden Grove Hall - Mottingham
Sessions:
4:45-5:15pm - Tiny Sparks
5:15-6:45pm - Drama, Song & Dance ages 6-10 years
6:45- 8:15pm - Drama, Song & Dance ages 11- 18years

Day : Wednesdays
Venue : Hollybank Hall - Bexley Village
3:45-4:15pm - Tiny Sparks
4:30-6:00pm - ESD MT ages 6-10 years
6:00-7:30pm - ESD MT ages 11-18 years

Day: Fridays
Venue : The Hub, 217 Brackmoor Lane New Eltham
4:15-4:45 - Tiny Sparks
4:45-6:15pm - Drama, Song & Dance ages 6-10 years
6:15- 7:45pm - Drama, Song & Dance ages 11- 18years

Day: Saturdays
10am-2pm - Weekend Footlights Company ages 4-18 years
Junior & Senior groups

Target Market(s)

Parents and children ages 10- 18years

Industry/Entity Type

Performing Art

Colors
e34297
f04a50
f68e4e
faa54b

Requirements
Must have
• A full time table & class descriptions on the back
• Be bright and eye catching
• Bold wording
• Company logos as well as BRSVE logo & FQMR logo & NPGU logo
Nice to have
• Large pot ( the Star Quest one)
Should not have
• Look too cluttered

```html
<!DOCTYPE html>
<html lang="en">
<head>
<meta charset="utf-8">
<title>Every Stage Drama Academy – Timetable</title>
<link rel="stylesheet" href="https://fonts.googleapis.com/css2?family=Open+Sans:ital,wght@0,400;0,600;1,700&display=swap">
<style>
  :root {
    --sky: #a6d0f0;
    --paper: #ffffff;
    --ink: #1d1d1d;
    --price-bg: #231f20;
    --price-text: #ffffff;
    --band-start: #c52f48;
    --band-end: #763c8a;
    --rule: #2a2a2a;
  }
  * { margin: 0; padding: 0; box-sizing: border-box; }
  html, body { width: 1200px; height: 700px; overflow: hidden; }
  body {
    background: var(--sky);
    font-family: "Open Sans", Arial, sans-serif;
    color: var(--ink);
    position: relative;
  }
  .sheet {
    position: absolute; left: 229px; top: 0;
    width: 741px; height: 700px;
    background: var(--paper);
  }
  .grid-lines { position: absolute; left: 0; top: 0; width: 1200px; height: 600px; pointer-events: none; }
  .class-card { position: absolute; width: 300px; }
  .class-title {
    font-weight: 700; font-style: italic; font-size: 14.5px;
    line-height: 18px; letter-spacing: -0.1px;
  }
  .class-ages {
    position: absolute; left: 0;
    font-weight: 700; font-style: italic; font-size: 13.5px; line-height: 18px;
  }
  .class-desc {
    position: absolute; left: 0;
    font-size: 12.4px; line-height: 13.8px; letter-spacing: -0.25px;
    font-weight: 400;
  }
  .price {
    position: absolute; width: 108px; height: 21px;
    background: var(--price-bg); color: var(--price-text);
    font-weight: 700; font-style: italic; font-size: 18px; line-height: 21px;
    text-align: center; letter-spacing: 0.3px;
  }
  .days-band {
    position: absolute; left: 229px; top: 586px; width: 741px; height: 39px;
    background: linear-gradient(90deg, var(--band-start), var(--band-end));
    color: #fff; text-align: center;
    font-style: italic; font-weight: 400; font-size: 38px; line-height: 39px;
    letter-spacing: 0.5px;
  }
  .day-name {
    position: absolute; font-weight: 700; font-style: italic; font-size: 14.5px; line-height: 18px;
  }
  .day-venue {
    position: absolute; font-weight: 700; font-style: italic; font-size: 12.5px; line-height: 16px;
  }
</style>
</head>
<body>
  <div class="sheet"></div>

  <svg class="grid-lines" viewBox="0 0 1200 600" aria-hidden="true">
    <polygon points="270,138 576,136.8 880,138 576,139.2" fill="var(--rule)"/>
    <polygon points="278,326 576,325 890,326 576,327" fill="var(--rule)"/>
    <polygon points="575.6,0 576.4,0 576.6,550 575.4,550" fill="var(--rule)"/>
  </svg>

  <!-- Row 1 -->
  <section class="class-card" style="left:280px; top:-13px;">
    <h3 class="class-title">Tiny Sparks</h3>
    <p class="class-ages" style="top:30px;">Ages 3-5 years</p>
    <p class="class-desc" style="top:55px;">Drama, Singing &amp; Dance from Pellworth to<br>Pop in one fast paced fun &amp; imaginative<br>session with regular confidence building<br>shows</p>
  </section>
  <div class="price" style="left:446px; top:105px;">£4.00</div>

  <section class="class-card" style="left:603px; top:-13px;">
    <h3 class="class-title">Drama, Song &amp; Dance</h3>
    <p class="class-ages" style="top:30px;">Ages 6- 10 years</p>
    <p class="class-desc" style="top:55px;">90 minutes of complete theatrical training<br>taught by qualified industry experts with the<br>opportunity to take BRSVE &amp; FQMR Dance<br>exams, regular shows and local events</p>
  </section>
  <div class="price" style="left:769px; top:108px;">£8.50</div>

  <!-- Row 2 -->
  <section class="class-card" style="left:280px; top:152px;">
    <h3 class="class-title">Drama, Song &amp; Dance</h3>
    <p class="class-ages" style="top:28px;">Ages 11- 18 years</p>
    <p class="class-desc" style="top:53px;">90 minutes of advanced level Drama,<br>Singing and Dance. BRSVE &amp; FQMR dance<br>exams , shows, competitions and audition<br>preparation for colleges and castings. This<br>session is a one stop shop for professional<br>theatrical training.</p>
  </section>
  <div class="price" style="left:446px; top:296px;">£8.50</div>

  <section class="class-card" style="left:603px; top:152px;">
    <h3 class="class-title">ESD MT ( Musical Theatre)</h3>
    <p class="class-ages" style="top:28px;">Ages 6- 10 years</p>
    <p class="class-desc" style="top:53px;">90 minutes of advanced level Drama, Singing<br>and Dance. BRSVE &amp; FQMR dance exams , shows,<br>competitions and audition preparation for<br>colleges and castings. This session is a one stop<br>shop for professional theatrical training.</p>
  </section>
  <div class="price" style="left:773px; top:299px;">£8.50</div>

  <!-- Row 3 -->
  <section class="class-card" style="left:280px; top:337px;">
    <h3 class="class-title">ESD MT ( Musical Theatre)</h3>
    <p class="class-ages" style="top:28px;">Ages 11- 18 years</p>
    <p class="class-desc" style="top:53px;">90 minutes of professional Musical Theatre<br>training with an emphasis on singing.<br>These Chorale- Style sessions are ideal for<br>those who love musicals such as Hexbound,<br>Jukebox &amp; Grand Ringmaster. Our<br>advanced MT sessions produce high<br>quality songs &amp; medleys for shows<br>and competitions as well as Musical<br>Theatre/ Singing exams and Solo BRSVE<br>training.</p>
  </section>
  <div class="price" style="left:446px; top:542px;">£8.50</div>

  <section class="class-card" style="left:603px; top:337px;">
    <h3 class="class-title">Weekend Footlights Company</h3>
    <p class="class-ages" style="top:28px;">Ages 4- 18 years</p>
    <p class="class-desc" style="top:53px;">4 hours of professional training, working<br>towards a production. This unique group gives<br>young performers the opportunity to perform in<br>a full scale production EVERY term. Past shows<br>include 'Ferry Cousins', 'Kelani', 'Tiny Stall of<br>Frights', 'Anselm &amp; Corabel' and 'Pellworth<br>Heirlines' At ESD we believe that pupils<br>learn through actual performing experience,<br>there is a role for everyone, full costume and<br>the chance to shine on stage!</p>
  </section>
  <div class="price" style="left:773px; top:542px;">£20.00</div>

  <h2 class="days-band">Days:</h2>

  <h3 class="day-name" style="left:280px; top:643px;">Tuesdays</h3>
  <p class="day-venue" style="left:280px; top:674px;">Venue: Linden Grove Hall - Mottingham</p>

  <h3 class="day-name" style="left:603px; top:643px;">Fridays</h3>
  <p class="day-venue" style="left:603px; top:674px;">Venue : The Hub, 217 Brackmoor Lane New Eltham</p>
</body>
</html>
```